Hawaii Luxury Real Estate Sales Broker needs Stationery Design Project

I am a high end property Broker here in Hawaii. I am trying to distinguish myself and my name as a brand as opposed to just being one in hundreds of Realtors out there. I am fortunate to have positioned myself into this particular market and would like to continue to grow my business here by finding the right added touch of classy detail that will make me stand out to Buyers and Sellers of this caliber. I am looking to brand myself via stationary and ads that I can place internationally. The high net worth individuals that I will be reaching out to make this a project that needs to emulate class and sophistication but with a bit of a feminine appeal as I am a woman. :-) Because I live in Hawaii I think this too may be able to play a part of the elegance in design based on the beauty that surrounds us here in the Pacific.

Target Market(s)

High Net Worth Individuals (Calder List, Birch Rd Gazette, Private Jet owners)

Industry/Entity Type

Business

Requirements
Must have
• My initials. I would like to see my name or initials always at their fingertips as I want them to be thinking of me as their Realtor.
Should not have
• Nothing too cheesy or touristy. It is important that this is something I can confidently send to high net worth individuals.

```html
<!DOCTYPE html>
<html lang="en">
<head>
<meta charset="utf-8">
<title>Notepad – From the desk of Lani Mercer</title>
<link rel="stylesheet" href="https://fonts.googleapis.com/css2?family=Jost:wght@500&family=Kalam:wght@400&display=swap">
<style>
  :root {
    --backdrop: #e9e6df;
    --paper: #f3ecd6;
    --ink: #141414;
    --gold: #a88a3c;
  }
  * { margin: 0; padding: 0; box-sizing: border-box; }
  html, body {
    width: 985px;
    height: 1200px;
    overflow: hidden;
    background: var(--backdrop);
  }
  .canvas {
    position: relative;
    width: 985px;
    height: 1200px;
  }
  .notepad {
    position: absolute;
    left: 57px;
    top: 40px;
    width: 870px;
    height: 1120px;
    background: var(--paper);
  }
  .header {
    position: absolute;
    left: 0;
    top: 0;
    width: 100%;
    height: 300px;
  }
  .header__lead {
    position: absolute;
    left: 75px;
    top: 170px;
    font-family: "Kalam", cursive;
    font-size: 27px;
    line-height: 1;
    color: var(--ink);
  }
  .header__name {
    position: absolute;
    left: 340px;
    top: 160px;
    display: flex;
    align-items: center;
    gap: 16px;
  }
  .header__mark {
    width: 22px;
    height: 22px;
    background: var(--gold);
  }
  .header__wordmark {
    font-family: "Jost", sans-serif;
    font-weight: 500;
    font-size: 36px;
    letter-spacing: 0.22em;
    color: var(--ink);
    line-height: 1;
  }
</style>
</head>
<body>
  <main class="canvas">
    <section class="notepad">
      <header class="header">
        <p class="header__lead">From the desk of</p>
        <div class="header__name">
          <span class="header__mark" aria-hidden="true"></span>
          <h1 class="header__wordmark">LANI MERCER</h1>
        </div>
      </header>
    </section>
  </main>
</body>
</html>
```